Health Benefits Association Website Design

The Unified Household Wellspring Alliance (UHWA) is an organization formed for the purpose of providing its members better value for selected health benefits and services. Members can use the association benefits either in conjunction with or independently of other medical insurance they may have. Some of the benefits available include discounted dental and vision care and prescription mail order services. There is no limitation on who can join. This membership will be primarily marketed as a way to enhance the value of a fixed benefit health insurance plan although members do not have to have the insurance plan join the association.

We are seeking a design for a website to be used for consumers to get information about membership and for current members to be able to access their benefits. The website should include:

1) A landing page to provide a description of the UHWA

2) A secondary page that can be duplicated that will:
a. Provide a list of benefits
b. Provide a membership enrollment form
c. Provide a member’s only access page
d. Provide a contact page for more information

We are seeking a modern but conservative design that will reflect value, simplicity and good health. The site design will also need to be compatible for use with mobile phones and tablets.

A copy of the association logo is included with the submission. It will also need to be incorporated into the website design. Layouts of similar association websites have also been included for reference.

Target Market(s)

Ages 25 to 65 unmarried, married with no children, professionals, self-employed, active and healthy

Industry/Entity Type

Health And Wellness

Number of Pages Required

2 page

Font styles to use
Sans Serif

Colors

Designer to choose colors to be used in the design.

Requirements
Must have
• UHWA Logo (attached). Use colors from the logo in the website design.
Nice to have
• Graphics, if used, should convey health and fitness and skew toward a diverse array of adults 25 to 40.

```html
<!DOCTYPE html>
<html lang="en">
<head>
<meta charset="utf-8">
<title>Unified Household Wellspring Alliance</title>
<link href="https://fonts.googleapis.com/css2?family=Arimo:wght@400;700&family=Tinos:wght@400;700&display=swap" rel="stylesheet">
<style>
:root{
  --olive:#8c9b57;
  --olive-dark:#7d8c4b;
  --olive-soft:#a3ae74;
  --gold:#f6c400;
  --page:#f4f4f4;
  --text:#555;
  --heading:#6b6b5a;
  --btn-dark:#5d5d55;
  --white:#fff;
  --rule:#c9c9c9;
}
*{margin:0;padding:0;box-sizing:border-box}
html,body{width:1200px;height:2517px;overflow:hidden}
body{position:relative;background:var(--white);font-family:'Arimo',Arial,sans-serif;color:var(--text)}
.abs{position:absolute}
a{color:inherit;text-decoration:none}

.top-bar{left:0;top:0;width:1200px;height:34px;background:var(--olive);color:var(--white);font-size:13px;font-weight:700;letter-spacing:1px}
.top-bar .account{left:133px;top:9px}
.top-bar .account span{margin:0 22px}
.top-bar .search{left:868px;top:10px;font-size:12px;font-weight:400}
.top-bar svg{left:1025px;top:8px}

.brand{left:0;top:34px;width:1200px;height:220px;display:flex;align-items:center;justify-content:center;gap:14px}
.brand-mark{width:22px;height:22px;border-radius:50%;background:var(--gold)}
.brand-name{font-size:30px;font-weight:700;color:var(--olive);letter-spacing:.5px}

.main-nav{top:287px;font-size:19px;letter-spacing:1.5px;color:#555}
.main-nav.active{color:var(--olive)}
.social{top:282px;width:34px;height:34px;border-radius:50%;background:#333}
.social.first{background:#3b5998}

.hero-photo{left:0;top:334px;width:1200px;height:589px;background:linear-gradient(100deg,#cfe0e8 0%,#e9eef0 40%,#dfe6ea 70%,#b9c7cf 100%)}
.hero-band{left:0;top:795px;width:1200px;height:128px;background:rgba(140,155,87,.9)}
.hero-title{left:148px;top:808px;font-size:27px;font-weight:700;color:var(--white);letter-spacing:1.5px}
.hero-text{left:148px;top:845px;width:650px;font-size:13.5px;line-height:19px;color:var(--white)}
.hero-btn{left:826px;top:846px;width:159px;height:43px;border:2px solid var(--white);color:var(--white);font-size:17px;letter-spacing:1px;display:flex;align-items:center;justify-content:center}

.content{left:0;top:923px;width:1200px;height:983px;background:var(--page)}
.welcome-small{left:138px;top:970px;font-family:'Tinos',serif;font-size:22px;letter-spacing:1.5px;color:#444}
.welcome-title{left:138px;top:998px;font-family:'Tinos',serif;font-size:25px;font-weight:700;letter-spacing:2px;color:var(--olive)}
.rule{height:1px;background:var(--rule)}
.benefits-title{left:767px;top:998px;font-family:'Tinos',serif;font-size:25px;font-weight:700;letter-spacing:2px;color:var(--heading)}
.benefits-title span{color:var(--olive)}
.intro{left:160px;width:540px;font-size:14.5px;line-height:31.5px;color:#444;letter-spacing:.4px}
.intro em{font-style:normal;color:var(--olive)}

.services-bar{left:133px;top:1393px;width:585px;height:32px;background:var(--olive-soft);color:var(--white);font-size:15px;font-weight:700;letter-spacing:1px;padding:7px 0 0 25px}
.service-row{left:126px;width:590px;height:112px}
.service-row.highlight{background:#e9e9e9}
.service-icon{position:absolute;left:34px;top:28px}
.service-title{position:absolute;left:110px;top:26px;font-size:14.5px;font-weight:700;color:var(--olive);letter-spacing:.8px}
.service-text{position:absolute;left:110px;top:49px;width:455px;font-size:13.5px;line-height:17px;color:#555;letter-spacing:.4px}
.full-list{left:161px;top:1792px;width:154px;height:30px;background:var(--olive-soft);color:var(--white);font-size:12.5px;letter-spacing:.8px;display:flex;align-items:center;justify-content:center}

.card-photo{left:770px;width:294px;height:183px;border:3px solid #ddd;background:linear-gradient(90deg,#e4ebee,#c9d4d8 50%,#e8ecee)}
.card-title{left:770px;font-family:'Tinos',serif;font-size:15px;letter-spacing:1.3px;color:#444}
.card-text{left:770px;width:300px;font-size:12.5px;line-height:17px;color:#555}
.card-btn{left:770px;width:103px;height:30px;background:var(--btn-dark);color:var(--white);font-size:12.5px;display:flex;align-items:center;justify-content:center}

.testimonials{left:0;top:1906px;width:1200px;height:398px;background:linear-gradient(90deg,#b8bf8f 0%,#a9b17b 55%,#7f8a4f 100%)}
.testi-title{left:144px;top:1940px;font-family:'Tinos',serif;font-size:26px;font-weight:700;letter-spacing:2px;color:var(--white)}
.testi-rule{left:128px;top:1984px;width:942px;height:1px;background:rgba(255,255,255,.7)}
.testi-text{left:151px;top:1998px;width:900px;font-size:14px;line-height:31.5px;color:var(--white);letter-spacing:.5px}
.quote-box{left:151px;top:2107px;width:918px;height:131px;background:#f6f6f6}
.portrait{position:absolute;left:14px;top:10px;width:110px;height:110px;border-radius:50%;border:4px solid #ddd;background:radial-gradient(circle at 50% 45%,#e8c7a6,#c89a6a 70%)}
.quote-mark{position:absolute;left:128px;top:0;font-family:'Tinos',serif;font-size:60px;color:#ccc}
.quote-text{position:absolute;left:156px;top:28px;width:740px;font-size:24px;line-height:30px;color:#333;letter-spacing:.6px}
.quote-name{position:absolute;right:60px;top:98px;font-size:14px;font-weight:700;color:#444;letter-spacing:1px}

.newsletter{left:141px;top:2351px;width:926px;height:54px;border:1px solid #ddd;background:var(--white)}
.newsletter .label{position:absolute;left:26px;top:18px;font-size:13.5px;font-weight:700;letter-spacing:1.3px;color:#333}
.newsletter .field{position:absolute;left:326px;top:0;width:1px;height:52px;background:#ddd}
.newsletter .placeholder{position:absolute;left:348px;top:19px;font-size:13px;color:#666;letter-spacing:.5px}
.submit{position:absolute;left:714px;top:-1px;width:212px;height:54px;background:var(--gold);color:var(--white);font-size:14px;font-weight:700;letter-spacing:1.5px;display:flex;align-items:center;justify-content:center;gap:12px}
.footer-nav{top:2427px;font-size:14px;letter-spacing:1.2px;color:#444}

.bottom-bar{left:0;top:2477px;width:1200px;height:40px;background:var(--olive);color:var(--white);font-size:12px;letter-spacing:1px}
.bottom-bar .legal{left:140px;top:14px}
.bottom-bar .legal span{margin:0 18px}
.bottom-bar .dot{top:12px;width:17px;height:17px;border-radius:50%;background:var(--white)}
</style>
</head>
<body>

<header>
  <div class="abs top-bar">
    <div class="abs account"><a href="#">LOGIN</a><span>|</span><a href="#">REGISTER</a></div>
    <div class="abs search">SEARCH</div>
    <svg class="abs" width="18" height="18" viewBox="0 0 18 18"><circle cx="10" cy="7" r="5" fill="none" stroke="#fff" stroke-width="2"/><line x1="6.5" y1="10.5" x2="2" y2="15" stroke="#fff" stroke-width="2"/></svg>
  </div>

  <div class="abs brand">
    <span class="brand-mark"></span>
    <span class="brand-name">Unified Household Wellspring Alliance</span>
  </div>

  <nav>
    <a class="abs main-nav" style="left:148px" href="#">Home</a>
    <a class="abs main-nav" style="left:263px" href="#">About us</a>
    <a class="abs main-nav" style="left:411px" href="#">Benefits</a>
    <a class="abs main-nav active" style="left:555px" href="#">Our Services</a>
    <a class="abs main-nav" style="left:740px" href="#">Contact us</a>
    <span class="abs social first" style="left:902px"></span>
    <span class="abs social" style="left:941px"></span>
    <span class="abs social" style="left:983px"></span>
    <span class="abs social" style="left:1024px"></span>
  </nav>
</header>

<section>
  <div class="abs hero-photo" role="img" aria-label="Photo of a smiling nurse talking with a smiling patient in a bright clinic"></div>
  <div class="abs hero-band"></div>
  <h1 class="abs hero-title">Heading sample text goes here</h1>
  <p class="abs hero-text">Lorem ipsum dolor sit amet, consectetur adipiscing elit. Curabitur lacinia pretium risus ac euismod. Aliquam auctor convallis mattis. Maecenas ornare augue vel nibh molestie, nec ultrices velit tincidunt.</p>
  <a class="abs hero-btn" href="#">Read More</a>
</section>

<main>
  <div class="abs content"></div>

  <div class="abs welcome-small">Welcome to</div>
  <h2 class="abs welcome-title">Unified Household Wellspring Alliance</h2>
  <div class="abs rule" style="left:132px;top:1044px;width:591px"></div>

  <p class="abs intro" style="top:1075px">&nbsp;Lorem ipsum dolor sit amet, consectetur adipiscing elit. Fusce eget sem feugiat, <em>ullamcorper</em> nulla vitae, iaculis erat. Proin lacus magna, pharetra eget turpis in, imperdiet malesuada quam. Nunc accumsan ipsum metus, accumsan congue purus euismod sed.</p>
  <p class="abs intro" style="top:1233px">Vivamus auctor tristique feugiat. Class aptent taciti sociosqu ad litora torquent per conubia nostra, <em>per inceptos himenaeos</em>. Fusce eu lacus ac nisi fringilla blandit. Aliquam et feugiat orci. Vestibulum laoreet suscipit turpis quis convallis.</p>

  <div class="abs services-bar">List of services we offer</div>

  <div class="abs service-row" style="top:1446px">
    <svg class="service-icon" width="60" height="60" viewBox="0 0 60 60"><circle cx="30" cy="30" r="28" fill="none" stroke="#8c9b57" stroke-width="2.5"/><path d="M30 28c-3-5-10-3-8 2 1 3 8 7 8 7s7-4 8-7c2-5-5-7-8-2z" fill="#8c9b57"/><path d="M14 38c6 0 10 4 16 4s10-2 16-6" fill="none" stroke="#8c9b57" stroke-width="3" stroke-linecap="round"/></svg>
    <div class="service-title">Title of service goes here</div>
    <div class="service-text">Lorem ipsum dolor sit amet, consectetur adipiscing elit. Fusce eget sem feugiat, ullamcorper nulla vitae, iaculis erat.</div>
  </div>
  <div class="abs service-row highlight" style="top:1559px">
    <svg class="service-icon" width="60" height="60" viewBox="0 0 60 60"><circle cx="30" cy="30" r="28" fill="none" stroke="#8c9b57" stroke-width="2.5"/><circle cx="30" cy="15" r="4" fill="#8c9b57"/><path d="M30 21v16M30 26l-8 6M30 26l8-4M30 37l-6 12M30 37l5 12" stroke="#8c9b57" stroke-width="3" stroke-linecap="round" fill="none"/></svg>
    <div class="service-title">Title of service goes here</div>
    <div class="service-text">Lorem ipsum dolor sit amet, consectetur adipiscing elit. Fusce eget sem feugiat, ullamcorper nulla vitae, iaculis erat.</div>
  </div>
  <div class="abs service-row" style="top:1669px">
    <svg class="service-icon" width="60" height="60" viewBox="0 0 60 60"><circle cx="30" cy="30" r="28" fill="none" stroke="#8c9b57" stroke-width="2.5"/><circle cx="19" cy="24" r="4.5" fill="#8c9b57"/><circle cx="41" cy="24" r="4.5" fill="#8c9b57"/><circle cx="30" cy="21" r="5" fill="#8c9b57"/><path d="M11 40c0-6 4-10 8-10s8 4 8 10zM33 40c0-6 4-10 8-10s8 4 8 10zM20 42c0-8 5-13 10-13s10 5 10 13z" fill="#8c9b57"/></svg>
    <div class="service-title">Title of service goes here</div>
    <div class="service-text">Lorem ipsum dolor sit amet, consectetur adipiscing elit. Fusce eget sem feugiat, ullamcorper nulla vitae, iaculis erat.</div>
  </div>

  <a class="abs full-list" href="#">See the full list &nbsp;+</a>

  <h2 class="abs benefits-title">Member’s <span>Benefits</span></h2>
  <div class="abs rule" style="left:760px;top:1044px;width:314px"></div>

  <div class="abs card-photo" style="top:1084px" role="img" aria-label="Photo of a doctor reviewing a chart with a senior patient"></div>
  <div class="abs card-title" style="top:1286px">TITLE OF THIS LINK GOES HERE</div>
  <p class="abs card-text" style="top:1310px">Lorem ipsum dolor sit amet, consectetur adipiscing elit. Curabitur lacinia pretium risus ac euismod. A ictor convallis mattis.</p>
  <a class="abs card-btn" style="top:1373px" href="#">Read more</a>

  <div class="abs card-photo" style="top:1463px" role="img" aria-label="Photo of a doctor examining a patient's knee in a clinic"></div>
  <div class="abs card-title" style="top:1665px">TITLE OF THIS LINK GOES HERE</div>
  <p class="abs card-text" style="top:1689px">Lorem ipsum dolor sit amet, consectetur adipiscing elit. Curabitur lacinia pretium risus ac euismod. A ictor convallis mattis.</p>
  <a class="abs card-btn" style="top:1752px" href="#">Read more</a>
</main>

<section>
  <div class="abs testimonials" role="img" aria-label="Olive-tinted photo of a smiling member in a bright room"></div>
  <h2 class="abs testi-title">Member’s Testimonials</h2>
  <div class="abs testi-rule"></div>
  <p class="abs testi-text">Lorem ipsum dolor sit amet, consectetur adipiscing elit. Curabitur lacinia pretium risus ac euismod. A ictor convallis mattis. Maecenas ornare augue vel nibh molestie, nec ultrices velit tincidunt. Aliquam convallis mattis.Aliquam auctor Maecenas ornare augue vel nibh molestie, nec ultrices velit tincidunt.</p>
  <div class="abs quote-box">
    <div class="portrait" role="img" aria-label="Portrait photo of the member quoted"></div>
    <div class="quote-mark">“</div>
    <p class="quote-text">Lorem ipsum dolor sit amet, consectetur adipiscing elit. Curabitur lacinia pretium risus ac euismod.“</p>
    <div class="quote-name">- Mara Ellison</div>
  </div>
</section>

<footer>
  <form class="abs newsletter">
    <div class="label">SUBSCRIBE TO OUR NEWSLETTER</div>
    <div class="field"></div>
    <div class="placeholder">Enter your email address</div>
    <div class="submit">
      <svg width="24" height="18" viewBox="0 0 24 18"><ellipse cx="12" cy="9" rx="11" ry="8" fill="#fff"/><path d="M6 6l6 4 6-4" fill="none" stroke="#f6c400" stroke-width="2"/></svg>
      SUBMIT
    </div>
  </form>

  <a class="abs footer-nav" style="left:204px" href="#">Home</a>
  <a class="abs footer-nav" style="left:316px" href="#">About us</a>
  <a class="abs footer-nav" style="left:453px" href="#">Member’s Benefits</a>
  <a class="abs footer-nav" style="left:674px" href="#">Our Services</a>
  <a class="abs footer-nav" style="left:853px" href="#">Contact us</a>

  <div class="abs bottom-bar">
    <div class="abs legal">Privacy Policy<span>|</span>Terms &amp; Conditions<span>|</span>Copyright © 2017 UHWA</div>
    <span class="abs dot" style="left:968px"></span>
    <span class="abs dot" style="left:992px"></span>
    <span class="abs dot" style="left:1016px"></span>
    <span class="abs dot" style="left:1040px"></span>
  </div>
</footer>

</body>
</html>
```